I am looking for help designing my new business cards. I would like rounded edges and a raised logo on the back of the card. I have 2 Logos. One with a boat in it and one without. I'd like the one on the back to be the one that includes the boat and just the name on the front. I have included multiple formats of my logo. Please let me know if you need anymore.

Target Market(s)

Potential buyers and other sales brokers

Industry/Entity Type

Sales - Yacht / Boat Sales

Contact Information for Business Card

Id liike the front to include just the business name portion of the logo along with my name (Corwin Dalby), phone number (555.318.6027), website address (www.dalbymarineco.example) and not my physical address but just "Port Halden, SC". The back should include my full logo that has the boat included. This portion I'd prefer raised amd take up the majority of the space there. Thanks!!

Colors
0054AA
0677BA
7BADD7
CADEEF
E8F1F8
0094D4
00A9DD
6FCCEA
C7EBF8
E9F6FB

Requirements
Must have
• Double sided
Nice to have
• My email address: Corwin@dalbymarineco.example The NMTG logo somewhere small on the front of the card
Should not have
• My full address, prefer only "Port Halden, SC"

```html
<!DOCTYPE html>
<html lang="en">
<head>
<meta charset="utf-8">
<title>Dalby Marine Co – Business Card</title>
<link rel="stylesheet" href="https://fonts.googleapis.com/css2?family=Roboto:wght@500;700;900&display=swap">
<style>
  :root {
    --bg: #2f2d35;
    --navy: #1d3163;
    --sky: #7badd7;
    --paper: #ffffff;
    --ink: #1d3163;
  }
  * { margin: 0; padding: 0; box-sizing: border-box; }
  html, body { width: 1200px; height: 848px; overflow: hidden; }
  body {
    background: var(--bg);
    font-family: "Roboto", Arial, sans-serif;
    display: flex;
    flex-direction: column;
    align-items: center;
    justify-content: center;
    gap: 44px;
  }
  .card {
    position: relative;
    width: 525px;
    height: 300px;
    border-radius: 24px;
    overflow: hidden;
    box-shadow: 0 14px 30px rgba(0,0,0,.35);
  }

  /* Back side: large brand name */
  .card-back {
    background: var(--sky);
    display: flex;
    align-items: center;
    justify-content: center;
    gap: 18px;
  }
  .brand-mark-dot {
    width: 34px; height: 34px;
    border-radius: 50%;
    background: var(--navy);
  }
  .brand-name-large {
    color: var(--navy);
    font-weight: 900;
    font-size: 44px;
    letter-spacing: 1px;
    text-transform: uppercase;
  }

  /* Front side */
  .card-front { background: var(--paper); }
  .brand-name-small {
    position: absolute;
    top: 22px; right: 30px;
    color: var(--navy);
    font-weight: 900;
    font-size: 22px;
    letter-spacing: .5px;
    text-transform: uppercase;
  }
  .holder-name {
    position: absolute;
    left: 48px; top: 128px;
    color: var(--ink);
    font-weight: 900;
    font-size: 28px;
  }
  .contact-list {
    position: absolute;
    left: 270px; top: 66px;
    list-style: none;
  }
  .contact-item {
    display: flex;
    align-items: center;
    gap: 10px;
    height: 30px;
    color: var(--ink);
    font-weight: 500;
    font-size: 13.5px;
  }
  .contact-icon { width: 20px; height: 20px; flex: none; }
  .wave { position: absolute; left: 0; top: 0; width: 525px; height: 300px; }
</style>
</head>
<body>

  <section class="card card-back" aria-label="Card back">
    <span class="brand-mark-dot"></span>
    <span class="brand-name-large">Dalby Marine Co</span>
  </section>

  <section class="card card-front" aria-label="Card front">
    <svg class="wave" viewBox="0 0 525 300" aria-hidden="true">
      <path d="M0,244 C150,260 270,229 340,202 C410,176 470,172 525,180 L525,300 L0,300 Z" fill="var(--sky)"/>
      <path d="M0,230 C150,246 270,215 340,188 C410,162 470,158 525,166" fill="none" stroke="var(--navy)" stroke-width="2.5"/>
    </svg>

    <div class="brand-name-small">Dalby Marine Co</div>

    <h1 class="holder-name">Corwin Dalby</h1>

    <ul class="contact-list">
      <li class="contact-item">
        <svg class="contact-icon" viewBox="0 0 20 20" aria-hidden="true">
          <circle cx="10" cy="10" r="9" fill="none" stroke="var(--navy)" stroke-width="1.4"/>
          <path d="M10 15 C7 11.5 6.5 10 6.5 8.5 A3.5 3.5 0 0 1 13.5 8.5 C13.5 10 13 11.5 10 15Z" fill="none" stroke="var(--navy)" stroke-width="1.3"/>
          <circle cx="10" cy="8.5" r="1.2" fill="var(--navy)"/>
        </svg>
        Port Halden, SC
      </li>
      <li class="contact-item">
        <svg class="contact-icon" viewBox="0 0 20 20" aria-hidden="true">
          <circle cx="10" cy="10" r="9" fill="none" stroke="var(--navy)" stroke-width="1.4"/>
          <path d="M7 6 L8.6 6 L9.3 8 L8.3 9 C8.8 10.2 9.8 11.2 11 11.7 L12 10.7 L14 11.4 L14 13 C10 13.5 6.5 10 7 6Z" fill="var(--navy)"/>
        </svg>
        555.318.6027
      </li>
      <li class="contact-item">
        <svg class="contact-icon" viewBox="0 0 20 20" aria-hidden="true">
          <circle cx="10" cy="10" r="9" fill="none" stroke="var(--navy)" stroke-width="1.4"/>
          <rect x="5.5" y="7" width="9" height="6.5" fill="none" stroke="var(--navy)" stroke-width="1.3"/>
          <path d="M5.5 7 L10 11 L14.5 7" fill="none" stroke="var(--navy)" stroke-width="1.3"/>
        </svg>
        www.dalbymarineco.example
      </li>
    </ul>
  </section>

</body>
</html>
```